Kelvaro Wp design

We need a wordpress design that will incorporate a professional color scheme with company logo in a clean layout. The design needs to consider that this will be developed on a responsive theme. Colors are undetermined - can use different blue or red as highlight - creative use of colors will be important. Client wants a 'modern' look.

Industry/Entity Type

It Company

Font styles to use
Serif
Sans Serif

Colors

Designer to choose colors to be used in the design.

Requirements
Must have
• - Navigation: 1) Home 2) Real Estate For Sale 3) Auctions 4) About Us 5) Selling Your Property 6) Contact Us

Site will have slideshow - 1st image is attached.
Home Page Content:
My service, experience and dedication provide motivated Sellers and Buyers with a clear marketing advantage. I know that the only way to succeed in real estate is to provide more service than you can get anywhere else. And you will get that kind of service when you work with me.
I will provide you with the personal service you deserve. Put my professional image, reputation, and business ethics to work for you.

Header will have - Logo (attached) Contact Information. 2 Real Estate listing buttons on the right for "New Listings" and "Upcoming Auctions" - similar to http://www.plumtidehomes.example/home

and will have 4 call to action boxes- 1) Land 2) Residential 3) Commercial 4) Auctions

Footer will have site nav, smaller logo, and association logos (attached)
Nice to have
• use of dropdown menus

```html
<!DOCTYPE html>
<html lang="en">
<head>
<meta charset="utf-8">
<title>Kelvaro Realty LLC</title>
<link rel="stylesheet" href="https://fonts.googleapis.com/css2?family=Arimo:wght@400;700&family=Tinos:wght@400;700&display=swap">
<style>
:root{
  --red:#f00000;
  --red-dark:#c80000;
  --navy:#3d4270;
  --navy-dark:#2f3460;
  --blue:#0a77d0;
  --box-blue:#1f4a99;
  --page:#efefef;
  --ink:#222;
  --title:#3b3f6e;
  --white:#fff;
}
*{box-sizing:border-box;margin:0;padding:0}
html,body{width:1134px;height:1200px;overflow:hidden;background:var(--page)}
body{position:relative;font-family:Arimo,Arial,sans-serif;color:var(--ink)}
.abs{position:absolute}
.header{left:0;top:0;width:1134px;height:135px;background:linear-gradient(#ff0000 0%,#f20000 60%,#c70000 100%)}
.logo{left:104px;top:22px;display:flex;align-items:center;gap:10px}
.logo-dot{width:26px;height:26px;border-radius:50%;background:var(--navy)}
.logo-name{font-family:Tinos,serif;font-weight:700;font-size:30px;color:var(--white);letter-spacing:1px;line-height:1.1}
.call{right:95px;top:16px;font-size:16px;color:var(--white);text-shadow:0 1px 2px rgba(0,0,0,.5)}
.cta-btn{top:61px;height:42px;border-radius:8px;background:linear-gradient(#fff,#e6e6e6);box-shadow:2px 3px 3px rgba(0,0,0,.35);font-family:Tinos,serif;font-size:21px;color:#222;display:flex;align-items:center}
.cta-btn.listings{left:560px;width:203px;padding-left:70px}
.cta-btn.auctions{left:801px;width:238px;padding-left:62px}
.btn-icon{top:-4px;width:52px;height:46px;border-radius:4px}
.listings .btn-icon{left:-12px;background:linear-gradient(#d9a36b,#a0522d 55%,#7a8b3c)}
.auctions .btn-icon{left:0;background:linear-gradient(#e8262a 0 22%,#f4f7fb 22%,#c9d8ea)}
.nav{left:0;top:135px;width:1134px;height:51px;background:var(--navy);border-top:1px solid #5a5f8a;border-bottom:1px solid #ccd}
.nav-item{top:0;height:49px;line-height:49px;font-weight:700;font-size:15.5px;color:var(--white);transform:translateX(-50%);white-space:nowrap}
.nav-item.active{top:10px;height:33px;line-height:33px;padding:0 15px;background:var(--blue);border-radius:3px}
.nav-sep{top:10px;width:1px;height:32px;background:#5c618c}
.dropdown{left:429px;top:186px;width:148px;height:76px;background:var(--blue);padding:6px 5px}
.drop-item{height:31px;line-height:28px;padding-left:7px;font-size:14px;color:var(--white)}
.drop-item.current{background:#ff0000}
.hero{left:0;top:186px;width:1134px;height:381px;background:linear-gradient(#5a93d6 0%,#9cc2ea 40%,#d9d2c3 55%,#8f8a7a 68%,#5f8a2c 85%,#4f7a22 100%)}
.hero-bar{left:0;top:567px;width:1134px;height:51px;background:var(--blue);color:var(--white);font-family:Tinos,serif;text-shadow:1px 1px 2px rgba(0,0,0,.4)}
.hero-name{left:101px;top:11px;font-size:26px}
.hero-price{right:107px;top:8px;font-size:30px}
.welcome{left:0;top:638px;width:1134px;text-align:center;font-family:Tinos,serif;font-size:34px;color:var(--title)}
.intro{left:100px;top:698px;width:934px;text-align:center;font-size:14.6px;line-height:21px}
.intro p+p{margin-top:21px}
.card{top:828px;width:213px;height:181px;background:var(--box-blue);padding:0 8px}
.card-title{height:46px;line-height:50px;text-align:center;font-family:Tinos,serif;font-weight:700;font-size:24px;color:var(--white);letter-spacing:.5px;text-shadow:1px 1px 2px rgba(0,0,0,.6)}
.card-photo{width:197px;height:125px}
.land{background:linear-gradient(#b8d3ee 0 22%,#8a7a4a 30%,#9aa64c 45%,#b9b86a 100%)}
.residential{background:linear-gradient(#9dc3ea 0 15%,#9a6b55 30%,#8a5040 60%,#5a8a35 85%,#7aa84a 100%)}
.commercial{background:linear-gradient(90deg,#9a8d7e 0%,#c9c2b5 30%,#d7dde2 60%,#eef1f4 100%)}
.auction-photo{background:linear-gradient(#7a6a55 0%,#4a4e55 40%,#d6d0c8 100%)}
.footer{left:0;top:1049px;width:1134px;height:151px;background:var(--navy)}
.foot-nav{left:101px;top:35px;font-size:14px;color:var(--white);word-spacing:2px}
.foot-nav span{margin:0 9px}
.copyright{left:100px;top:75px;font-size:14px;color:#e4e5ee}
.badge{top:24px;height:45px;background:#151515;border-radius:3px}
.foot-logo{left:849px;top:80px;display:flex;align-items:center;gap:7px}
.foot-logo .logo-dot{width:16px;height:16px;background:#bbb}
.foot-logo .logo-name{font-size:19px;color:#dcdcdc}
</style>
</head>
<body>
<header class="header abs">
  <div class="logo abs"><span class="logo-dot"></span><span class="logo-name">KELVARO REALTY, LLC</span></div>
  <div class="call abs">Call Us Today:&nbsp; Kelvaro (555) 014-2290&nbsp; Kelvaro (555) 018-4471</div>
  <div class="cta-btn listings abs"><span class="btn-icon abs" role="img" aria-label="Small house icon with New tag"></span>New Listings</div>
  <div class="cta-btn auctions abs"><span class="btn-icon abs" role="img" aria-label="Calendar icon"></span>Upcoming Auctions</div>
</header>

<section class="hero abs" role="img" aria-label="Slideshow photo of a single-storey stucco house with a red tile roof, gravel drive and trees"></section>
<div class="hero-bar abs"><span class="hero-name abs">Kelvaro Realty LLC</span><span class="hero-price abs">$ 90,000</span></div>

<nav class="nav abs">
  <span class="nav-item abs" style="left:143px">Home</span>
  <span class="nav-sep abs" style="left:197px"></span>
  <span class="nav-item abs" style="left:303px">Real Estate For Sale</span>
  <span class="nav-sep abs" style="left:411px"></span>
  <span class="nav-item active abs" style="left:477px">Auctions</span>
  <span class="nav-sep abs" style="left:541px"></span>
  <span class="nav-item abs" style="left:608px">About Us</span>
  <span class="nav-sep abs" style="left:672px"></span>
  <span class="nav-item abs" style="left:786px">Selling Your Property</span>
  <span class="nav-sep abs" style="left:899px"></span>
  <span class="nav-item abs" style="left:971px">Contact Us</span>
</nav>
<div class="dropdown abs">
  <div class="drop-item">Upcoming Auction</div>
  <div class="drop-item current">Past Auction</div>
</div>

<h1 class="welcome abs" style="font-weight:400">Welcome to Kelvaro Realty LLC</h1>
<div class="intro abs">
  <p>My service, experience and dedication provide motivated Sellers and Buyers with a clear marketing advantage. I know that the only way to succeed in real estate is to provide more service than you can get anywhere else. And you will get that kind of service when you work with me.</p>
  <p>I will provide you with the personal service you deserve. Put my professional image, reputation, and business ethics to work for you.</p>
</div>

<div class="card abs" style="left:95px"><div class="card-title">Land</div><div class="card-photo land" role="img" aria-label="Photo of an open field with a wooden fence"></div></div>
<div class="card abs" style="left:338px"><div class="card-title">Residential</div><div class="card-photo residential" role="img" aria-label="Photo of a two-storey brick family home"></div></div>
<div class="card abs" style="left:585px"><div class="card-title">Commercial</div><div class="card-photo commercial" role="img" aria-label="Photo of a modern office building"></div></div>
<div class="card abs" style="left:826px"><div class="card-title">Auctions</div><div class="card-photo auction-photo" role="img" aria-label="Photo of a crowd gathered at an auction"></div></div>

<footer class="footer abs">
  <div class="foot-nav abs">Home<span>|</span>Real Estate For Sale<span>|</span>Auctions<span>|</span>About Us<span>|</span>Selling Your Property<span>|</span>Contact Us</div>
  <div class="copyright abs">Copyright © 2014 Kelvaro Realty,LLC . All rights reserved.</div>
  <span class="badge abs" style="left:775px;width:42px" role="img" aria-label="Association badge"></span>
  <span class="badge abs" style="left:831px;width:88px" role="img" aria-label="Association badge"></span>
  <span class="badge abs" style="left:934px;width:40px" role="img" aria-label="Association badge"></span>
  <span class="badge abs" style="left:991px;width:42px" role="img" aria-label="Association badge"></span>
  <div class="foot-logo abs"><span class="logo-dot"></span><span class="logo-name">KELVARO REALTY, LLC</span></div>
</footer>
</body>
</html>
```